Stationary & Business Cards
Brimford Holdings
Project: Stationary & Business Cards
Stationary & Business Cards - Construction
Creative Brief
Simple
Dale Purcott
General Manager
P.O. Box 382 Ashbury CT 06218
Dale@BrimfordHoldings.com
ON THE STATIONARY ONLY: add our website www.BrimfordHoldings.com
logo to fill in entire back of business card. (Red background with blue lettering)

```html
<!DOCTYPE html>
<html lang="en">
<head>
<meta charset="utf-8">
<title>Brimford Holdings – Business Card</title>
<link rel="stylesheet" href="https://fonts.googleapis.com/css2?family=Roboto:wght@400;500;900&display=swap">
<style>
  :root {
    --navy: #23407f;
    --red: #e0313b;
    --white: #ffffff;
    --page: #e9ebef;
    --text-light: #ffffff;
  }
  html, body {
    margin: 0;
    padding: 0;
    width: 1200px;
    height: 901px;
    overflow: hidden;
    background: var(--page);
    font-family: "Roboto", Arial, sans-serif;
  }
  .canvas {
    position: relative;
    width: 1200px;
    height: 901px;
  }
  .business-card {
    position: absolute;
    left: 150px;
    top: 193px;
    width: 900px;
    height: 514px;
    border-radius: 44px;
    overflow: hidden;
    background: var(--white);
    box-shadow: 0 10px 30px rgba(0,0,0,0.15);
  }
  .card-shapes {
    position: absolute;
    inset: 0;
  }
  .brand-name {
    position: absolute;
    left: 62px;
    top: 70px;
    margin: 0;
    font-weight: 900;
    font-size: 54px;
    letter-spacing: 1px;
    text-transform: uppercase;
    color: var(--navy);
    line-height: 1;
  }
  .holder {
    position: absolute;
    left: 90px;
    top: 318px;
    color: var(--text-light);
  }
  .holder-name {
    margin: 0;
    font-size: 30px;
    font-weight: 400;
  }
  .holder-title {
    margin: 6px 0 0;
    font-size: 22px;
    font-weight: 400;
  }
  .contact-list {
    position: absolute;
    left: 568px;
    top: 338px;
    margin: 0;
    padding: 0;
    list-style: none;
    color: var(--text-light);
    font-size: 17px;
    line-height: 1.25;
  }
  .contact-list li {
    display: flex;
    align-items: center;
    gap: 9px;
    margin-bottom: 2px;
  }
  .contact-list .gap-after { margin-bottom: 12px; }
  .contact-icon {
    width: 15px;
    height: 15px;
    flex: none;
  }
</style>
</head>
<body>
<main class="canvas">
  <article class="business-card">
    <svg class="card-shapes" width="900" height="514" viewBox="0 0 900 514" aria-hidden="true">
      <path d="M0 205 Q 450 250 900 300 L900 514 L0 514 Z" fill="var(--red)"/>
      <path d="M0 220 Q 450 268 900 320 L900 514 L0 514 Z" fill="var(--navy)"/>
      <polygon points="150,220 180,223 158,244" fill="var(--navy)"/>
    </svg>

    <h1 class="brand-name">Brimford Holdings</h1>

    <div class="holder">
      <p class="holder-name">Dale Purcott</p>
      <p class="holder-title">General Manager</p>
    </div>

    <ul class="contact-list">
      <li class="gap-after">
        <svg class="contact-icon" viewBox="0 0 16 16"><circle cx="8" cy="8" r="8" fill="#fff"/><path d="M8 3.5a3 3 0 0 0-3 3c0 2.2 3 5.5 3 5.5s3-3.3 3-5.5a3 3 0 0 0-3-3z" fill="var(--navy)"/><circle cx="8" cy="6.5" r="1.1" fill="#fff"/></svg>
        <span>P.O. Box 382 Ashbury CT 06218</span>
      </li>
      <li>
        <svg class="contact-icon" viewBox="0 0 16 16"><circle cx="8" cy="8" r="8" fill="#fff"/><path d="M5 4.5l1.6-.4 1 2.2-1 .8a5 5 0 0 0 2.3 2.3l.8-1 2.2 1-.4 1.6c-3.5.3-6.8-3-6.5-6.5z" fill="var(--navy)"/></svg>
        <span>555-014-2290</span>
      </li>
      <li>
        <svg class="contact-icon" viewBox="0 0 16 16"><circle cx="8" cy="8" r="8" fill="#fff"/><rect x="5.5" y="3.5" width="5" height="9" rx="1" fill="var(--navy)"/></svg>
        <span>555-014-2291</span>
      </li>
      <li class="gap-after">
        <svg class="contact-icon" viewBox="0 0 16 16"><circle cx="8" cy="8" r="8" fill="#fff"/><rect x="4" y="6" width="8" height="5" fill="var(--navy)"/><rect x="5.5" y="3.5" width="5" height="2.5" fill="var(--navy)"/></svg>
        <span>555-014-2292</span>
      </li>
      <li>
        <svg class="contact-icon" viewBox="0 0 16 16"><circle cx="8" cy="8" r="8" fill="#fff"/><rect x="4" y="5" width="8" height="6" fill="var(--navy)"/><path d="M4 5l4 3.2L12 5" fill="none" stroke="#fff" stroke-width="0.9"/></svg>
        <span>Dale@BrimfordHoldings.com</span>
      </li>
      <li>
        <svg class="contact-icon" viewBox="0 0 16 16"><circle cx="8" cy="8" r="8" fill="#fff"/><circle cx="8" cy="8" r="4" fill="none" stroke="var(--navy)" stroke-width="1.2"/><path d="M4 8h8M8 4c-2 2.5-2 5.5 0 8M8 4c2 2.5 2 5.5 0 8" fill="none" stroke="var(--navy)" stroke-width="0.9"/></svg>
        <span>www.BrimfordHoldings.com</span>
      </li>
    </ul>
  </article>
</main>
</body>
</html>
```